Flyer-Design für die Gleichstellungsstelle einer kommunalen Stadtverwaltung
Zielgruppe
Wir sind die Gleichstellungsstelle einer kommunalen Stadtverwaltung (Einwohner*innen ca. 74.500) und richten uns mit unserer Arbeit grundsätzlich an alle Menschen. Wir möchten einen übersichtlichen Flyer haben, der die wichtigsten Rahmenbedingungen unserer Arbeit erläutert und Kontaktdaten enthält (z.B. sollen neue Mitarbeiter*innen der Verwaltung den Flyer erhalten).
Aufgabenstellung
- Der Flyer soll im Format DIN A6 sein, die Rückseite (Text) im Hochformat, die Vorderseite kann im Hoch- oder Querformat sein.
- Die Vorderseite soll gestaltet werden. Die Auswahl / Gestaltung liegt in der Kreativität der Designer*innen.
- Das Bild auf der Vorderseite kann auch eine Wortwolke kann, muss aber nicht! Begriffe für eine mögliche Wortwolke sind in an angehängten Dateien zu finden.
- Auf der Rückseite muss das angehängte Logo der Gleichstellungsstelle gemäß Corporate Design enthalten sein.
- Außer bei Fotos ist möglichst auf die Farbwelt des Corporate Designs zu achten.
- Schriftart gemäß Corporate Design (wenn möglich Avenir Next, alternativ Arial oder ähnliche Schrift).

```html
<!DOCTYPE html>
<html lang="de">
<head>
<meta charset="utf-8">
<title>Gleichstellungsstelle – Flyer Vorderseite</title>
<link rel="stylesheet" href="https://fonts.googleapis.com/css2?family=Mulish:wght@400;500;800&display=swap">
<style>
  :root {
    --rose: #d17f7f;
    --wine: #7e3b3a;
    --white: #ffffff;
    --tone-dark: #3a2a2c;
    --tone-slate: #5f5468;
    --tone-brown: #a8583f;
    --tone-berry: #8c3a3e;
    --tone-coral: #c85c5c;
  }
  * { margin: 0; padding: 0; box-sizing: border-box; }
  html, body { width: 1200px; height: 851px; overflow: hidden; }
  body { background: var(--rose); font-family: "Mulish", "Avenir Next", Arial, sans-serif; }

  .flyer-front {
    position: relative;
    width: 1200px;
    height: 851px;
    background: var(--rose);
    overflow: hidden;
  }

  .quote {
    position: absolute;
    top: 103px;
    left: 0;
    width: 1200px;
    text-align: center;
    color: var(--white);
    font-weight: 500;
    font-size: 51px;
    line-height: 68px;
    letter-spacing: 0.5px;
    text-transform: uppercase;
  }
  .quote-line { display: block; }
  .quote-highlight { color: var(--wine); font-weight: 800; }

  .quote-author {
    position: absolute;
    top: 320px;
    left: 752px;
    color: var(--white);
    font-size: 27px;
    font-weight: 400;
    letter-spacing: 0.3px;
  }

  .people-illustration {
    position: absolute;
    left: 0;
    top: 440px;
    width: 1200px;
    height: 411px;
  }
</style>
</head>
<body>
  <main class="flyer-front">
    <p class="quote">
      <span class="quote-line">Es wird keine</span>
      <span class="quote-line"><span class="quote-highlight">Gleichberechtig</span> geben,</span>
      <span class="quote-line">solange alles gleich bleibt.</span>
    </p>
    <p class="quote-author">Selin Aydemir</p>

    <svg class="people-illustration" viewBox="0 0 1200 411" role="img"
         aria-label="Illustration: eine Gruppe von fünf Frauen unterschiedlicher Herkunft, nebeneinander stehend">
      <defs>
        <linearGradient id="people-tones" x1="0" y1="0" x2="1" y2="0">
          <stop offset="0" stop-color="var(--tone-dark)"/>
          <stop offset="0.25" stop-color="var(--tone-slate)"/>
          <stop offset="0.5" stop-color="var(--tone-brown)"/>
          <stop offset="0.72" stop-color="var(--tone-berry)"/>
          <stop offset="1" stop-color="var(--tone-coral)"/>
        </linearGradient>
        <linearGradient id="people-fade" x1="0" y1="0" x2="0" y2="1">
          <stop offset="0" stop-color="var(--rose)" stop-opacity="1"/>
          <stop offset="0.35" stop-color="var(--rose)" stop-opacity="0"/>
        </linearGradient>
      </defs>
      <rect width="1200" height="411" fill="url(#people-tones)"/>
      <rect width="1200" height="411" fill="url(#people-fade)"/>
    </svg>
  </main>
</body>
</html>
```